Insurance Firm needs Stationary and Corporate Identity

We have a logo (provided) - we need a business card, letterhead, booklet cover, Benefit & Travel card design, and brand guide.
KTR (Kestrel Trust Reinsurers) is a National (Canadian) family-run benefits firm. We've been providing alternative benefit models to small and medium sized businesses for almost 25 years! Our goal is to create long-lasting customer relationships by partnering with our clients to become their dedicated benefits division instead of just selling a product to them.

Benefit & Travel Cards: We provide the benefit card to employees to allow them to pay for drugs at their pharmacy and dental services electronically.
The travel card is for medical emergencies while travelling outside of Canada.

Brand Guide: Once the stationary is complete, the brand guide will allow us to streamline the use of our logo's and fonts for internal and external use. We will expect that this will be a paid project for our design winner after the contest closes and we will negotiate the pricetag for this at that time.

Target Market(s)

Business Owners, Entrepreneurs, HR Professionals

Industry/Entity Type

Insurance Agency

Font styles to use
Sans Serif

Requirements
Must have
• business card, letterhead, health card, travel card, booklet cover (some current samples provided)

```html
<!DOCTYPE html>
<html lang="en">
<head>
<meta charset="utf-8">
<title>Kestrel Trust Reinsurers — Stationery</title>
<link href="https://fonts.googleapis.com/css2?family=Montserrat:wght@400;500;600&family=Lora:wght@400&display=swap" rel="stylesheet">
<style>
  :root{
    --navy:#28315a;
    --navy-deep:#222a4e;
    --red:#e3222c;
    --grey:#a9abb0;
    --paper:#f7f7fa;
    --backdrop:#e4e4e6;
  }
  *{box-sizing:border-box;margin:0;padding:0}
  html,body{width:1200px;height:1200px;overflow:hidden;background:var(--backdrop)}
  body{position:relative;font-family:"Montserrat",sans-serif}
  .piece{position:absolute;overflow:hidden}
  .piece .art{position:absolute;inset:0;width:100%;height:100%}
  .wordmark{position:absolute;font-weight:600;color:var(--grey);letter-spacing:.02em;line-height:1;white-space:nowrap}
  .wordmark small{display:block;font-weight:600;font-size:.28em;letter-spacing:.04em;margin-top:.35em;text-transform:uppercase}

  /* Booklet cover */
  .booklet{left:60px;top:60px;width:520px;height:300px;background:var(--navy)}
  .booklet .stitch{position:absolute;inset:16px;border:2px dashed #c9cbd3;border-radius:14px}
  .booklet .watermark{position:absolute;left:130px;top:70px;font-weight:600;font-size:150px;color:#3a4369;line-height:1}

  /* Letterhead */
  .letterhead{left:640px;top:60px;width:440px;height:620px;background:var(--paper)}
  .letterhead .wordmark{left:26px;top:22px;font-size:34px;color:#ffffff}
  .letterhead .wordmark small{font-size:8px;color:#c9cbd3}
  .letterhead .watermark{position:absolute;left:60px;top:250px;font-weight:600;font-size:150px;color:#dcdde2;line-height:1}

  /* Envelope */
  .envelope{left:60px;top:400px;width:520px;height:280px;background:var(--navy)}
  .envelope .wordmark{left:36px;top:170px;font-size:46px}
  .envelope .wordmark small{font-size:11px;color:var(--grey)}

  /* Business card front */
  .card-front{left:60px;top:740px;width:420px;height:240px;background:var(--navy)}
  .card-front .wordmark{left:0;right:0;top:78px;text-align:center;font-size:56px}
  .card-front .wordmark small{font-size:12px}

  /* Business card back */
  .card-back{left:520px;top:740px;width:420px;height:240px;background:var(--navy)}
  .card-back .wordmark{left:24px;top:98px;font-size:34px}
  .card-back .wordmark small{font-size:7px}
  .contacts{position:absolute;right:22px;top:38px;list-style:none;font-family:"Lora",serif;font-size:12px;line-height:1.35;color:#e6e7ee;text-align:right}
  .contacts li{display:flex;align-items:center;justify-content:flex-end;gap:10px;min-height:32px}
  .contacts .dot{width:18px;height:18px;border-radius:50%;background:var(--red);flex:none;display:flex;align-items:center;justify-content:center}
  .contacts .dot svg{width:10px;height:10px;display:block}
</style>
</head>
<body>

<section class="piece booklet" aria-label="Booklet cover">
  <div class="watermark">KTR</div>
  <div class="stitch"></div>
</section>

<section class="piece letterhead" aria-label="Letterhead">
  <svg class="art" viewBox="0 0 440 620" preserveAspectRatio="none">
    <path d="M0 0H440V90H0Z" fill="var(--navy)"/>
    <path d="M205 0Q195 50 175 100" stroke="#ffffff" stroke-width="1.5" fill="none"/>
    <path d="M0 560Q90 520 140 560T440 520V620H0Z" fill="var(--navy)"/>
    <path d="M0 554Q90 514 140 554T440 514" stroke="var(--red)" stroke-width="3" fill="none"/>
  </svg>
  <div class="watermark">KTR</div>
  <div class="wordmark">KTR<small>Kestrel Trust Reinsurers</small></div>
</section>

<section class="piece envelope" aria-label="Envelope">
  <svg class="art" viewBox="0 0 520 280" preserveAspectRatio="none">
    <path d="M0 0H520L260 130Z" fill="var(--navy-deep)"/>
    <path d="M36 250H490" stroke="var(--red)" stroke-width="3"/>
  </svg>
  <div class="wordmark">KTR<small>Kestrel Trust Reinsurers</small></div>
</section>

<section class="piece card-front" aria-label="Business card front">
  <svg class="art" viewBox="0 0 420 240" preserveAspectRatio="none">
    <path d="M0 0H40Q20 120 40 240H0Z" fill="var(--red)"/>
    <path d="M420 0H380Q400 120 380 240H420Z" fill="var(--red)"/>
  </svg>
  <div class="wordmark">KTR<small>Kestrel Trust Reinsurers</small></div>
</section>

<section class="piece card-back" aria-label="Business card back">
  <svg class="art" viewBox="0 0 420 240" preserveAspectRatio="none">
    <path d="M200 0Q172 90 200 130Q162 170 172 240H160Q150 170 188 130Q160 90 188 0Z" fill="var(--red)"/>
  </svg>
  <div class="wordmark">KTR<small>Kestrel Trust Reinsurers</small></div>
  <ul class="contacts">
    <li><span>+123 456 789<br>+123 456 789</span><span class="dot"><svg viewBox="0 0 10 10"><path d="M2 1L4 3L3 4Q4 6 6 7L7 6L9 8L8 9Q3 9 1 2Z" fill="#fff"/></svg></span></li>
    <li><span>hello@kestreltrust.ca</span><span class="dot"><svg viewBox="0 0 10 10"><rect x="1" y="2.5" width="8" height="5" fill="none" stroke="#fff"/><path d="M1 2.5L5 6L9 2.5" fill="none" stroke="#fff"/></svg></span></li>
    <li><span>social.kestreltrust.ca</span><span class="dot"></span></li>
    <li><span>kestreltrust.ca</span><span class="dot"><svg viewBox="0 0 10 10"><circle cx="5" cy="5" r="3.8" fill="none" stroke="#fff"/><path d="M1.2 5H8.8M5 1.2V8.8" stroke="#fff"/></svg></span></li>
    <li><span>Your Address, Street,<br>city, Country.</span><span class="dot"><svg viewBox="0 0 10 10"><path d="M5 9L2 5A3 3 0 1 1 8 5Z" fill="#fff"/></svg></span></li>
  </ul>
</section>

</body>
</html>
```